Eye Institute Needs New Look

I have very detailed notes to guide you but be creative where needed. Attached are a screenshot of a wp theme i like and how i would like most content cut out and certain parts used. Site should be in blues.

Their current site is CLEARVALEOPTIC.com and you can pull some content and their logo from there (sorry, that is the best i can get from them for logo)

the theme I like is: http://brintor-sample.com/velmora_wp/

but review attached notes to see changes I want and direction of website.

All of the designs are VERY well done and followed instructions well.  They all are very similar and what I was looking for.  But all designers made two consistent mistakes.  For any that wish to be considered and still in the running for the final decision, I need these two changes to your submissions:

1) the designs are too clean / white.  I was looking for the content areas to be shades of blue , dark blue, etc so that the new site design isn't white and clean like their current site.

2) the boxes under the header.  I have seen versions with the grays and blues.  Can we try it with some bold multi colors for pop like red, yellow, green, orange, etc?

3) overall, this is an example site they liked http://www.mypeltonvision.com/ , can you get the site to have some splash of a bold complimentary highlight color and less overall white in the site?

Thank you and I look forward to submissions.  I need to show the client tomorrow so hopefully anyone still considering can get me revisions in the next 12 hours.

```html
<!DOCTYPE html>
<html lang="en">
<head>
<meta charset="utf-8">
<title>Clearvale Optic Institute</title>
<link href="https://fonts.googleapis.com/css2?family=Roboto+Condensed:wght@300;400;700&family=Arimo:wght@400;700&family=Ubuntu:wght@400;500&display=swap" rel="stylesheet">
<style>
:root{
  --blue:#2f9ae6;
  --blue-light:#45aef0;
  --navy:#1a5c91;
  --content-blue:#1d5f9c;
  --feature-blue:#143f6a;
  --feature-ink:#d6e6f5;
  --accent:#ffa21f;
  --box-red:#e2402b;
  --box-yellow:#e3a400;
  --box-green:#3a9f45;
  --box-orange:#ee7418;
  --footer:#262626;
  --footer-head:#303030;
  --white:#fff;
}
*{margin:0;padding:0;box-sizing:border-box}
html,body{width:767px;height:1200px;overflow:hidden;background:var(--content-blue)}
body{position:relative;font-family:"Arimo",sans-serif;color:#444}
.abs{position:absolute}

/* header */
.site-header{left:0;top:0;width:767px;height:64px;background:linear-gradient(180deg,#3aa3ea,#2f94de)}
.brand{left:58px;top:13px;color:var(--white);font-family:"Roboto Condensed",sans-serif;font-weight:700;font-size:18px;line-height:1;display:flex;align-items:center;gap:7px}
.brand-dot{width:12px;height:12px;border-radius:50%;background:var(--white)}
.social{top:8px;display:block;width:19px;height:19px;border-radius:50%;background:var(--white)}
.call{left:566px;top:8px;color:var(--white);font-family:"Roboto Condensed",sans-serif;font-size:14px;letter-spacing:.2px}
.main-nav{left:305px;top:38px;display:flex;align-items:center;font-family:"Ubuntu",sans-serif;font-size:9px;color:var(--white);text-transform:uppercase}
.main-nav a{color:inherit;text-decoration:none;padding:5px 8px;margin-right:2px}
.main-nav a.active{background:var(--navy);padding:5px 9px}
.main-nav .caret{font-size:8px;margin-left:3px}

/* hero */
.hero{left:0;top:64px;width:767px;height:416px;background:linear-gradient(180deg,#5c7f68 0%,#8a6a52 35%,#6fa7b8 65%,#3f8fae 100%)}
.hero-arrow{top:192px;width:20px;height:32px}
.hero-tag{left:429px;top:154px;padding:2px 6px;background:var(--blue);color:var(--white);font-family:"Roboto Condensed",sans-serif;font-weight:300;font-size:22px;letter-spacing:.3px}
.hero-caption{left:429px;top:184px;width:236px;height:78px;background:rgba(60,60,60,.72);padding:8px 10px;color:var(--white);font-family:"Roboto Condensed",sans-serif}
.hero-caption h2{font-weight:400;font-size:15px;letter-spacing:.4px}
.hero-caption p{font-weight:300;font-size:14px;line-height:20px;margin-top:1px}
.hero-dots{left:354px;top:394px;display:flex;gap:5px}
.hero-dots span{width:7px;height:7px;border-radius:50%;background:rgba(255,255,255,.6)}
.hero-dots span.on{background:var(--white)}

/* cta band */
.cta-band{left:0;top:480px;width:767px;height:46px;background:linear-gradient(180deg,#2d8fd8,#2a7fc4)}
.cta-band p{position:absolute;left:57px;top:13px;color:var(--white);font-family:"Roboto Condensed",sans-serif;font-weight:300;font-size:15px}
.cta-btn{position:absolute;left:620px;top:13px;width:90px;height:21px;background:var(--white);border-radius:2px;color:#333;font-family:"Roboto Condensed",sans-serif;font-size:12px;text-align:center;line-height:21px;letter-spacing:.3px}

/* process boxes */
.process{left:58px;top:538px;width:652px;height:141px;display:flex}
.process-box{width:163px;height:141px;color:var(--white);text-align:center;position:relative;padding-top:14px}
.process-box.laser{background:var(--box-yellow)}
.process-box.glaucoma{background:var(--box-green)}
.process-box.shop{background:var(--box-orange)}
.process-box svg{display:block;margin:0 auto}
.process-box h4{font-family:"Roboto Condensed",sans-serif;font-weight:400;font-size:12px;letter-spacing:.6px;margin-top:10px}
.process-box p{font-family:"Ubuntu",sans-serif;font-size:8.3px;line-height:13px;padding:0 13px;margin-top:7px}
.process-box.process-intro{background:var(--box-red);text-align:left;padding:12px 13px}
.process-box.process-intro h3{font-family:"Roboto Condensed",sans-serif;font-weight:300;font-size:13px;line-height:17px;letter-spacing:.2px}
.process-box.process-intro p{padding:0;margin-top:5px;font-size:8.2px;line-height:13px}
.process-box.process-intro .more{display:block;font-family:"Ubuntu",sans-serif;font-weight:500;font-size:7.5px;margin-top:9px}
.notch{position:absolute;right:-5px;top:0;width:0;height:0;border-top:6px solid transparent;border-bottom:6px solid transparent;border-left:5px solid var(--box-red);z-index:2}

/* feature */
.feature{left:0;top:692px;width:767px;height:159px;background:var(--feature-blue)}
.feature h2{position:absolute;left:58px;top:11px;color:var(--accent);font-family:"Roboto Condensed",sans-serif;font-weight:300;font-size:15px;letter-spacing:.2px}
.feature h2 sup{font-size:8px}
.feature .col-left{position:absolute;left:57px;top:34px;width:235px;font-size:8px;line-height:14px;color:var(--feature-ink)}
.feature .photo{position:absolute;left:313px;top:30px;width:141px;height:99px;border:3px solid var(--accent);background:linear-gradient(135deg,#9fb9c8,#6d8796 60%,#3f5564)}
.feature .col-right{position:absolute;left:479px;top:11px;width:232px;font-size:8px;line-height:14px;color:var(--feature-ink)}
.feature .link{display:block;margin-top:14px;color:var(--accent);font-size:8px}

/* footer */
.footer{left:0;top:870px;width:767px;height:330px;background:var(--footer);border-top:3px solid #1a1a1a}
.footer-head{position:absolute;left:0;top:0;width:767px;height:42px;background:var(--footer-head);border-bottom:1px solid #1d1d1d}
.footer-head h5{position:absolute;top:16px;color:#e9e9e9;font-family:"Arimo",sans-serif;font-weight:700;font-size:9.5px;letter-spacing:.3px}
.testimonial{position:absolute;left:78px;top:59px;width:140px;color:#d8d8d8;font-size:7.6px;line-height:11.5px}
.testimonial cite{display:block;font-style:normal}
.link-list{position:absolute;list-style:none;font-size:7.6px;color:#e3e3e3}
.link-list li{height:20px;line-height:20px;border-bottom:1px solid #3b3b3b;padding-left:4px}
.link-list li::before{content:"›";margin-right:6px;color:#bbb}
.map{position:absolute;left:396px;top:62px;width:135px;height:136px;background:linear-gradient(160deg,#5d8fd6,#4677c4);border-radius:4px}
.map-label{position:absolute;left:396px;top:80px;width:125px;color:var(--white);font-size:9.2px;line-height:11px}
.copyright-rule{position:absolute;left:78px;top:218px;width:612px;height:1px;background:#3b3b3b}
.copyright{position:absolute;left:78px;top:231px;color:#d6d6d6;font-size:7.5px}
.back-top{position:absolute;left:654px;top:231px;color:#d6d6d6;font-size:7.5px}
.seo{position:absolute;left:78px;top:255px;width:614px;color:#7e7e7e;font-size:7.4px;line-height:11.6px;text-align:justify}
</style>
</head>
<body>

<header class="site-header abs">
  <div class="brand abs"><span class="brand-dot"></span>Clearvale Optic Institute</div>
  <span class="social abs" style="left:506px" aria-label="Social link"></span>
  <span class="social abs" style="left:533px" aria-label="Social link"></span>
  <div class="call abs">Call Now : (555) 310-4826</div>
  <nav class="main-nav abs">
    <a class="active">Home</a>
    <a>Our Practice<span class="caret">&#8964;</span></a>
    <a>Services<span class="caret">&#8964;</span></a>
    <a>Education<span class="caret">&#8964;</span></a>
    <a style="margin-right:16px">Locations</a>
    <a>Contact</a>
  </nav>
</header>

<section class="hero abs" role="img" aria-label="Photo of four friends in swimwear jumping together into a resort pool">
  <svg class="hero-arrow abs" style="left:56px" viewBox="0 0 20 32"><path d="M16 2 4 16l12 14" fill="none" stroke="rgba(255,255,255,.8)" stroke-width="3"/></svg>
  <svg class="hero-arrow abs" style="left:692px" viewBox="0 0 20 32"><path d="M4 2l12 14L4 30" fill="none" stroke="rgba(255,255,255,.8)" stroke-width="3"/></svg>
  <div class="hero-tag abs">LASIK SURGERY</div>
  <div class="hero-caption abs">
    <h2>TRUSTED</h2>
    <p>Why are people trusting Clearvale Optic Institute for their eyecare?</p>
  </div>
  <div class="hero-dots abs"><span></span><span></span><span class="on"></span><span></span></div>
</section>

<section class="cta-band abs">
  <p>Make an appointment today at any of our convenient Michigan offices!</p>
  <div class="cta-btn">LOCATIONS</div>
</section>

<section class="process abs">
  <div class="process-box process-intro">
    <h3>OUR WORKING PROCESS<br>IN 3 STEPS</h3>
    <p>Sed ut perspiciatis unde omnis iste natus error sit voluptatem accusan-tium doloremque laudantium, totam rem aperiam, eaque ipsa quae ab illo inventore veritatis et</p>
    <span class="more">MORE ABOUT US +</span>
    <span class="notch"></span>
  </div>
  <div class="process-box laser">
    <svg width="24" height="32" viewBox="0 0 24 32" fill="none" stroke="#fff" stroke-width="1.3"><path d="M12 12v19M12 12 3 4M12 12l9-8M12 12 1 11M12 12l11-1M12 12 7 2M12 12l5-10M12 12l-8 6M12 12l8 6"/></svg>
    <h4>LASER</h4>
    <p>Sed ut perspiciatis unde omnis iste natus error sit voluptatem accu santium doloremque lau dantium, totam rem</p>
  </div>
  <div class="process-box glaucoma">
    <svg width="32" height="32" viewBox="0 0 32 32"><path d="M2 16c4-7 9-10 14-10s10 3 14 10c-4 7-9 10-14 10S6 23 2 16z" fill="none" stroke="#fff" stroke-width="2.4"/><circle cx="16" cy="16" r="4.5" fill="#fff"/></svg>
    <h4>GLAUCOMA</h4>
    <p>Sed ut perspiciatis unde omnis iste natus error sit voluptatem accu santium doloremque lau dantium, totam rem</p>
  </div>
  <div class="process-box shop">
    <svg width="34" height="32" viewBox="0 0 34 32" fill="none" stroke="#fff" stroke-width="2"><path d="M1 3h6l5 18h17l3-13H9"/><path d="M12 11h18M13 15h15" stroke-width="1.4"/><circle cx="14" cy="27" r="2.2" fill="#fff"/><circle cx="26" cy="27" r="2.2" fill="#fff"/></svg>
    <h4>EYE SHOP</h4>
    <p>Sed ut perspiciatis unde omnis iste natus error sit voluptatem accu santium doloremque lau dantium, totam rem</p>
  </div>
</section>

<section class="feature abs">
  <h2>PRESENTING THE LUMA SYSTEM<sup>®</sup></h2>
  <p class="col-left">LUMA, Brightwave® Refractive Analysis, is a revolutionary dia-gnostic device with Brightwave technology that is designed to take intraoperative wavefront aberrometry to a higher level of performance. The Brightwave technology has a precise light source and optics, the assurance of a live display of the eye, a convenient system-aligned, on-demand reticle and optimized algorithms to guide every refractive decision you make for your cataract patients.</p>
  <div class="photo" role="img" aria-label="Photo of a surgeon operating a surgical microscope in an operating room"></div>
  <div class="col-right">
    <p>Lumetric® not only wanted to improve upon its previous intraoperative aberrometry platform; they wanted to advance the entire category. The result is the LUMA System – the only intraoperative device that can provide you with refractive guidance to select the power of the IOL, determine the magnitude and axis of astigmatism and provide aphakic and pseudophakic measurements.</p>
    <span class="link">See the Unique Benefits of the LUMA System +</span>
  </div>
</section>

<footer class="footer abs">
  <div class="footer-head">
    <h5 style="left:78px">TESTIMONIALS</h5>
    <h5 style="left:237px">NAVIGATION</h5>
    <h5 style="left:396px">LOCATIONS</h5>
    <h5 style="left:555px">CONTACT US</h5>
  </div>
  <blockquote class="testimonial">"After my cataract surgery...it was absolutely phenominal. My eyesight was restored back to normal. It's been nine years (since my cataract surgery), and I haven't worn glasses ever since. It was so comfortable, there was no pain involved."<cite>&nbsp;&nbsp;— Daniel R., <i>Sterling Heights, Michigan</i></cite></blockquote>
  <ul class="link-list" style="left:237px;top:54px;width:136px">
    <li>Home</li><li>Appointment Request</li><li>Our Practice</li><li>Resources</li><li>Locations</li><li>Contact</li>
  </ul>
  <div class="map" role="img" aria-label="Map of Michigan's lower peninsula marking office locations"></div>
  <p class="map-label">Visit us at any of our convenient locations!</p>
  <ul class="link-list" style="left:555px;top:54px;width:136px">
    <li>Schedule an appointment</li><li>Go to our contact page</li>
  </ul>
  <div class="copyright-rule"></div>
  <p class="copyright">Copyright © 2011 Clearvale Optic Institute. All rights reserved.</p>
  <p class="back-top">back to top</p>
  <p class="seo">Clearvale Optic Institute offers patient a variety of Ophthalmology, Refractive &amp; Cosmetic Services including, LASIK surgery, Eye Exams, Glaucoma Diagnosis &amp; Treatment, Cataract Surgery, Interocular Lens Placement (IOL's), Treatment for Diabetic Retinopathy, Retinal Surgery, Treatment for Macular Degeration, Corneal Transplants, Relaxa, Firmatone, SilkContour Cellulite Treatment, Lumifill &amp; Eye Lid Surgery. Serving patients in the Detroit Michigan area including, Sterling Heights &amp; Chesterfield Township.</p>
</footer>

</body>
</html>
```